Business Card design for sports marketing creative agency

We need a business card designed for a sports marketing agency.
Side 1: Vosk | 720
Gold Vosk 720 brand
Division of Vosk | a creative agency that focuses on athletes
Modern look
Info on Card:
vosk720.com
@vosk_720
Peter R. Lund
Director of Client Services
M: 555.287.4193
E. peter@vosk720.com
Side 2:
Red Vosk | a creative agency brand
Marketing Creative Agency
Modern look
Info on card:
Vosk | a creative agency (red logo)
voskstudio.com
@voskstudio
Target Market(s)
Pro athletes
Industry/Entity Type
Marketing
Look and feel
Each slider illustrates characteristics of the customer's brand and the style your logo design should communicate.

```html
<!DOCTYPE html>
<html lang="en">
<head>
<meta charset="utf-8">
<title>Vosk 720 – Business Cards</title>
<link rel="stylesheet" href="https://fonts.googleapis.com/css2?family=Questrial&family=Montserrat:wght@400;700&display=swap">
<style>
  :root {
    --backdrop: #e9e6e2;
    --card-black: #0d1012;
    --card-black-soft: #161a1d;
    --brand-red: #e0263a;
    --strip-red: #c8101e;
    --brand-gold: #c9a94f;
    --gold-band: #d4b866;
    --ink-dark: #141414;
    --ghost: rgba(255, 255, 255, 0.06);
  }
  * { margin: 0; padding: 0; box-sizing: border-box; }
  html, body { width: 1200px; height: 800px; overflow: hidden; }
  body {
    background: var(--backdrop);
    position: relative;
    font-family: "Questrial", sans-serif;
  }

  .card {
    position: absolute;
    overflow: hidden;
    box-shadow: 0 14px 30px rgba(0, 0, 0, 0.25);
  }

  /* ---------- Agency card (red, portrait) ---------- */
  .agency-card {
    left: 130px; top: 110px;
    width: 330px; height: 580px;
    background: var(--strip-red);
  }
  .agency-card .side-strip {
    position: absolute; left: 0; top: 0;
    width: 52px; height: 100%;
    display: flex; align-items: center; justify-content: center;
  }
  .agency-card .side-strip span {
    transform: rotate(-90deg);
    white-space: nowrap;
    font-family: "Questrial", sans-serif;
    font-size: 15px; letter-spacing: 4px;
    color: var(--ink-dark);
  }
  .agency-card .panel {
    position: absolute; left: 52px; top: 22px; right: 0; bottom: 0;
    background: linear-gradient(160deg, var(--card-black-soft), var(--card-black));
    border-top-left-radius: 40px;
    overflow: hidden;
  }
  .agency-card .ghost-mark {
    position: absolute; left: 20px; top: 60px;
    transform-origin: left top;
    transform: rotate(90deg) translate(0, -190px);
    font-size: 190px; line-height: 1;
    color: var(--ghost);
    white-space: nowrap;
  }
  .agency-card .brand-mark {
    position: absolute; left: 56px; top: 20px;
    font-size: 86px; line-height: 1;
    color: var(--brand-red);
  }
  .agency-card .divider {
    position: absolute; left: 148px; top: 122px;
    width: 3px; height: 40px; background: var(--brand-red);
  }
  .agency-card .tagline {
    position: absolute; left: 162px; top: 176px;
    transform-origin: left top;
    transform: rotate(90deg) translate(0, -28px);
    font-size: 31px; color: var(--brand-red);
    white-space: nowrap;
  }

  /* ---------- Division card (gold, landscape) ---------- */
  .division-card {
    left: 520px; top: 250px;
    width: 580px; height: 330px;
    background: var(--gold-band);
  }
  .division-card .panel {
    position: absolute; left: 0; top: 0; right: 16px; bottom: 44px;
    background: linear-gradient(150deg, var(--card-black-soft), var(--card-black));
    border-bottom-right-radius: 40px;
    overflow: hidden;
  }
  .division-card .ghost-mark {
    position: absolute; right: -20px; bottom: -30px;
    font-size: 200px; line-height: 1;
    color: var(--ghost);
  }
  .division-card .brand-lockup {
    position: absolute; left: 34px; top: 24px;
    display: flex; align-items: flex-end;
    color: var(--brand-gold);
  }
  .division-card .brand-mark { font-size: 72px; line-height: 0.9; }
  .division-card .divider {
    width: 2px; height: 52px; background: var(--brand-gold);
    margin: 0 10px 0 14px;
  }
  .division-card .brand-number { font-size: 34px; line-height: 1; }
  .division-card .contact {
    position: absolute; left: 34px; top: 128px;
    font-family: "Montserrat", sans-serif;
    color: var(--brand-gold);
  }
  .division-card .contact .person {
    font-weight: 700; font-size: 17px; letter-spacing: 1px;
    text-transform: uppercase;
  }
  .division-card .contact .role { font-size: 13px; margin: 4px 0 12px; }
  .division-card .contact .line { font-size: 13px; line-height: 1.5; }
  .division-card .contact .label { font-weight: 700; margin-right: 6px; }
  .division-card .footer-band {
    position: absolute; left: 0; bottom: 0; width: 100%; height: 44px;
    display: flex; align-items: center; padding-left: 36px;
    font-family: "Questrial", sans-serif;
    font-size: 16px; letter-spacing: 4px;
    color: var(--ink-dark);
  }
  .division-card .footer-band .sep { margin: 0 18px; }
</style>
</head>
<body>

  <section class="card agency-card">
    <div class="side-strip"><span>voskstudio.com &nbsp;|&nbsp; @voskstudio</span></div>
    <div class="panel">
      <div class="ghost-mark" aria-hidden="true">Vosk</div>
      <div class="brand-mark">Vosk</div>
      <div class="divider"></div>
      <div class="tagline">a creative agency</div>
    </div>
  </section>

  <section class="card division-card">
    <div class="panel">
      <div class="ghost-mark" aria-hidden="true">Vosk</div>
      <div class="brand-lockup">
        <span class="brand-mark">Vosk</span>
        <span class="divider"></span>
        <span class="brand-number">720</span>
      </div>
      <div class="contact">
        <div class="person">Peter R. Lund</div>
        <div class="role">Director of Client Services</div>
        <div class="line"><span class="label">P:</span>555.287.4193</div>
        <div class="line"><span class="label">E:</span>peter@vosk720.com</div>
      </div>
    </div>
    <div class="footer-band">
      <span>vosk720.com</span><span class="sep">|</span><span>@vosk_720</span>
    </div>
  </section>

</body>
</html>
```